Re-Design of a 1 Pager IT Security Website

Please create a 1 Pager design for this website and all its elements: http://www.pelmarokvistaqueen.com/

Colours, Fonts etc: You can select whatever you prefer

```html
<!DOCTYPE html>
<html lang="en">
<head>
<meta charset="utf-8">
<title>Domain Monitoring</title>
<link href="https://fonts.googleapis.com/css2?family=Exo+2:wght@500;600;700&family=Nunito+Sans:wght@400;600;700&display=swap" rel="stylesheet">
<style>
:root{
  --bg-hero:#03124a;
  --bg-deep:#020c33;
  --bg-mid:#04164f;
  --bg-field:#0a1c5a;
  --cyan:#05dbe8;
  --cyan-link:#19c8e6;
  --white:#ffffff;
  --muted:#d6def5;
  --line:#1d3475;
}
*{box-sizing:border-box;margin:0;padding:0}
html,body{width:1200px;height:4162px;overflow:hidden}
body{background:var(--bg-deep);color:var(--white);font-family:"Nunito Sans",Arial,sans-serif;position:relative}
.abs{position:absolute}
h1,h2,h3,.heading{font-family:"Exo 2",Arial,sans-serif;font-weight:700;text-transform:uppercase;color:var(--white)}
.btn{position:absolute;display:flex;align-items:center;justify-content:center;background:var(--cyan);color:var(--white);border-radius:26px;font-family:"Exo 2",Arial,sans-serif;font-weight:600;font-size:16px;text-transform:uppercase;text-decoration:none}
.rule{position:absolute;height:4px;width:44px;background:var(--cyan);border-radius:2px}
.p{position:absolute;font-size:15.5px;line-height:30px;color:var(--muted)}
.center{text-align:center}

/* sections */
.hero{position:absolute;left:0;top:0;width:1200px;height:678px;background:radial-gradient(circle at 75% 35%,#0a3aa0 0%,#062a80 25%,var(--bg-hero) 60%)}
.risk{position:absolute;left:0;top:678px;width:1200px;height:784px;background:var(--bg-deep)}
.protect{position:absolute;left:0;top:1462px;width:1200px;height:538px;background:var(--bg-mid)}
.monitor{position:absolute;left:0;top:2000px;width:1200px;height:650px;background:var(--bg-deep)}
.about{position:absolute;left:0;top:2650px;width:1200px;height:450px;background:var(--bg-deep)}
.contact{position:absolute;left:0;top:3100px;width:1200px;height:663px;background:var(--bg-deep)}
.footer{position:absolute;left:0;top:3763px;width:1200px;height:399px;background:#031040}

/* header */
.brand{position:absolute;left:110px;top:30px;font-family:"Exo 2",Arial,sans-serif;font-weight:600;font-size:23px}
.nav a{position:absolute;top:35px;font-size:15px;font-weight:600;color:var(--white);text-decoration:none}
.nav a.active{color:var(--cyan)}

.hero-title{position:absolute;left:108px;top:212px;font-size:40px;line-height:48px;letter-spacing:.5px}
.hero-art{position:absolute;left:630px;top:97px;width:570px;height:565px;border-radius:40%;background:radial-gradient(circle at 55% 45%,#14a6f0 0%,#0a5fcf 35%,rgba(6,40,128,0) 70%)}

/* risk */
.section-title{position:absolute;left:0;width:1200px;text-align:center;font-size:31px}
.risk-card{position:absolute;width:290px;text-align:center}
.risk-icon{position:absolute;width:116px;height:116px;border-radius:50%;background:var(--cyan)}
.risk-card h3{font-size:18px;font-weight:600;margin-top:0}
.risk-card .rule{left:123px}
.risk-card p{position:absolute;top:56px;left:0;width:290px;font-size:14.5px;line-height:25.5px;color:var(--muted)}
.risk-card .more{position:absolute;top:198px;left:0;width:290px;font-family:"Exo 2",Arial,sans-serif;font-size:15px;color:var(--cyan-link);text-decoration:underline}
.divider{position:absolute;top:436px;width:1px;height:218px;background:var(--line)}

.protect-art{position:absolute;left:32px;top:64px;width:477px;height:404px;border-radius:45%;background:radial-gradient(circle at 50% 50%,#1b6fe0 0%,#0b3a9c 45%,rgba(4,22,79,0) 72%)}
.globe-art{position:absolute;left:622px;top:83px;width:541px;height:437px;border-radius:50%;background:radial-gradient(circle at 50% 50%,#1556a8 0%,#0a2f78 45%,rgba(2,12,51,0) 70%)}
.network-art{position:absolute;left:0;top:160px;width:1200px;height:220px;background:linear-gradient(180deg,rgba(2,12,51,0) 0%,rgba(30,70,150,.35) 50%,rgba(2,12,51,0) 100%)}

.ticks li{list-style:none;position:absolute;left:112px;font-size:15.5px;color:var(--muted);padding-left:29px}
.ticks svg{position:absolute;left:3px;top:3px}

/* contact form */
.field{position:absolute;background:var(--bg-field);color:var(--muted);font-size:15px;display:flex;align-items:center;padding-left:18px;gap:9px}
.field.msg{align-items:flex-start;padding-top:20px}

/* footer */
.f-head{position:absolute;top:84px;font-family:"Exo 2",Arial,sans-serif;font-weight:600;font-size:15px;line-height:22px;text-transform:uppercase}
.f-text{position:absolute;font-size:12px;line-height:19px;color:var(--muted)}
.f-links a{position:absolute;left:979px;font-size:15px;color:var(--muted);text-decoration:none}
.f-links a.active{color:var(--cyan)}
.social{position:absolute;top:240px;width:25px;height:25px;border-radius:50%;border:2px solid var(--cyan)}
.copy{position:absolute;top:344px;left:0;width:1200px;text-align:center;font-size:12px;color:var(--muted)}
.copy a{color:var(--cyan);text-decoration:underline}
</style>
</head>
<body>

<section class="hero">
  <div class="brand">Domain Monitoring</div>
  <nav class="nav">
    <a class="active" style="left:577px" href="#">Home</a>
    <a style="left:664px" href="#">About Us</a>
    <a style="left:774px" href="#">Our Services</a>
    <a style="left:906px" href="#">Our Blog</a>
    <a style="left:1012px" href="#">Contact Us</a>
  </nav>
  <div class="hero-art" role="img" aria-label="Glowing laptop with a protective shield and data dashboards"></div>
  <h1 class="hero-title">Prevent attacks by<br>monitoring your domains</h1>
  <p class="p" style="left:111px;top:319px;width:520px;line-height:26px;color:var(--white)">Lorem ipsum dolor sit amet, consectetur adipiscing elit, sed do eiusmod tempor incididunt ut labore et dolore magna aliqua.</p>
  <a class="btn" href="#" style="left:111px;top:396px;width:165px;height:51px;font-size:14px">Get Started</a>
</section>

<section class="risk">
  <h2 class="section-title" style="top:68px">What is the risk?</h2>
  <div class="rule" style="left:578px;top:116px"></div>
  <p class="p center" style="left:170px;top:142px;width:860px">Hackers use domain-based attacks, which are designed to trick users into submitting sensitive data or downloading dangerous files. This is often the case with phishing attacks. For example, domains can be registered that are very similar to one’s own company, a customer or a supplier. Once a fraudulent domain is registered, the hackers try to lure the employee to the website. This can be done via e-mail, SMS (smishing), instant messaging. Social media and many other techniques succeed. A distinction is made between different types of attacks:</p>

  <div class="risk-icon" style="left:228px;top:335px" role="img" aria-label="Browser window icon"></div>
  <div class="risk-icon" style="left:536px;top:335px" role="img" aria-label="Hooded hacker icon"></div>
  <div class="risk-icon" style="left:845px;top:335px" role="img" aria-label="Broken shield icon"></div>

  <div class="divider" style="left:441px"></div>
  <div class="divider" style="left:756px"></div>

  <div class="risk-card" style="left:141px;top:473px">
    <h3>Domain Spoofing</h3><div class="rule" style="top:36px"></div>
    <p>Here, a domain name is registered that resembles that of a trusted brand or organization. For example, the hacker can register the domain "trustpay-access.</p>
    <a class="more" href="#">Learn More</a>
  </div>
  <div class="risk-card" style="left:450px;top:473px">
    <h3>Homoglyphic Attack</h3><div class="rule" style="top:36px"></div>
    <p style="left:30px;width:230px">This is a variant of domain spoofing. Again, a similar looking domain is registered. But one uses characters outside the Latin alphabet</p>
    <a class="more" href="#">Learn More</a>
  </div>
  <div class="risk-card" style="left:758px;top:473px">
    <h3>Typosquatting</h3><div class="rule" style="top:36px"></div>
    <p style="left:30px;width:230px">cybercriminals may attempt to register a malicious domain by using a common misspelling of the target company’s domain. For example, someone might reserve</p>
    <a class="more" href="#">Learn More</a>
  </div>
</section>

<section class="protect">
  <div class="protect-art" role="img" aria-label="Isometric illustration of a hacker at a laptop inside a cylinder of data screens"></div>
  <h2 class="heading abs" style="left:538px;top:96px;font-size:34px">How to protect yourself?</h2>
  <p class="p" style="left:538px;top:157px;width:560px;color:var(--white)">Our domain monitoring solution continuously monitors thousands of TLDs, gTLDs and ccTLDs. For searches, we offer the greatest flexibility in the market and cover ALL forms of attacks. Here are a few examples of search options that can be adopted as active alerts:<br><span style="color:var(--cyan-link)">https://wiki.varnex.example/docs/search?</span>id=domain_database_search</p>
  <a class="btn" href="#" style="left:536px;top:327px;width:166px;height:52px">Learn More</a>
</section>

<section class="monitor">
  <h2 class="heading abs" style="left:112px;top:90px;font-size:34px;line-height:45px">What else are we<br>monitoring?</h2>
  <p class="p" style="left:112px;top:191px;width:490px;color:var(--white)">Varnex helps you understand when, where and how stolen or accidentally leaked information in dark web markets, forums, botnet logs, IRC, social media and other sources is exposed. Varnex’s alerting service can also detect threats before they turn into incidents. Varnex offers AI-driven dark web analysis, real-time threat alerts and pre-Attack threat indicators. Setup in minutes you will receive instant access to real-time reporting including:</p>
  <ul class="ticks">
    <li style="top:425px"><svg width="14" height="14" viewBox="0 0 14 14"><circle cx="7" cy="7" r="7" fill="#05dbe8"/><path d="M3.8 7.2l2.2 2.1 4.2-4.4" stroke="#020c33" stroke-width="1.8" fill="none"/></svg>Infrastructure exposure: IOT, RepoHub, CloudVault, CodeBin &amp; more</li>
    <li style="top:455px"><svg width="14" height="14" viewBox="0 0 14 14"><circle cx="7" cy="7" r="7" fill="#05dbe8"/><path d="M3.8 7.2l2.2 2.1 4.2-4.4" stroke="#020c33" stroke-width="1.8" fill="none"/></svg>People exposure: Social media monitoring</li>
  </ul>
  <a class="btn" href="#" style="left:120px;top:503px;width:165px;height:52px">Learn More</a>
  <div class="globe-art" role="img" aria-label="Digital globe with a glowing shield and connected user markers"></div>
</section>

<section class="about">
  <div class="network-art" role="img" aria-label="Faint network of connected points"></div>
  <h2 class="section-title" style="top:56px;font-size:34px">About Us</h2>
  <p class="p center" style="left:205px;top:119px;width:790px;color:var(--white)">Varnex (company registration number CHE-418.702.519) was started in 2018 as a public limited company in Zug, Switzerland. Our analysts have long-standing relationships with various players on the Darknet. These personal relationships make it possible for Varnex to repeatedly obtain the latest data leaks. Those unique data leaks are published by the press around the world.</p>
  <a class="btn" href="#" style="left:517px;top:262px;width:165px;height:52px">Learn More</a>
</section>

<section class="contact">
  <h2 class="section-title" style="top:76px;font-size:31px">Contact Us</h2>
  <p class="p center" style="left:215px;top:128px;width:770px;line-height:26px;color:var(--white)">Lorem ipsum dolor sit amet, consectetur adipiscing elit, sed do eiusmod tempor incididunt ut labore et dolore magna aliqua. Quis ipsum suspendisse ultrices gravida.</p>
  <div class="field" style="left:110px;top:240px;width:313px;height:52px"><svg width="14" height="14" viewBox="0 0 14 14" fill="none" stroke="#fff" stroke-width="1.4"><circle cx="7" cy="4.5" r="3"/><path d="M1.5 13.5c0-3 2.5-5 5.5-5s5.5 2 5.5 5"/></svg>Name</div>
  <div class="field" style="left:442px;top:240px;width:314px;height:52px"><svg width="15" height="12" viewBox="0 0 15 12" fill="none" stroke="#fff" stroke-width="1.4"><rect x="1" y="1" width="13" height="10"/><path d="M1 1l6.5 5.5L14 1"/></svg>Email</div>
  <div class="field" style="left:774px;top:240px;width:313px;height:52px"><svg width="14" height="14" viewBox="0 0 14 14" fill="none" stroke="#fff" stroke-width="1.4"><path d="M3 1l2.5 3-1.5 1.5c1 2 2.5 3.5 4.5 4.5L10 8.5l3 2.5-1.5 2C6 13 1 8 1 2.5z"/></svg>Phone</div>
  <div class="field msg" style="left:110px;top:311px;width:977px;height:162px"><svg width="15" height="14" viewBox="0 0 15 14" fill="none" stroke="#fff" stroke-width="1.4"><ellipse cx="7.5" cy="6" rx="6.5" ry="5"/><path d="M3 10l-1.5 3 4-1.8"/></svg>Message</div>
  <a class="btn" href="#" style="left:496px;top:518px;width:183px;height:48px;font-size:15px">Send Message</a>
</section>

<footer class="footer">
  <div class="f-head" style="left:113px">Contact Us</div>
  <svg class="abs" style="left:115px;top:123px" width="10" height="13" viewBox="0 0 10 13"><path d="M5 0a5 5 0 0 0-5 5c0 3.5 5 8 5 8s5-4.5 5-8a5 5 0 0 0-5-5z" fill="#05dbe8"/><circle cx="5" cy="5" r="1.8" fill="#031040"/></svg>
  <p class="f-text" style="left:135px;top:118px;width:180px">Domain Monitoring 15 B &nbsp;Lorem ipsum dolor sit</p>
  <svg class="abs" style="left:115px;top:173px" width="11" height="11" viewBox="0 0 14 14" fill="#05dbe8"><path d="M3 1l2.5 3-1.5 1.5c1 2 2.5 3.5 4.5 4.5L10 8.5l3 2.5-1.5 2C6 13 1 8 1 2.5z"/></svg>
  <p class="f-text" style="left:135px;top:170px">Phone:<br>+1 555 010 0199</p>
  <svg class="abs" style="left:114px;top:221px" width="12" height="10" viewBox="0 0 15 12" fill="none" stroke="#05dbe8" stroke-width="1.6"><rect x="1" y="1" width="13" height="10"/><path d="M1 1l6.5 5.5L14 1"/></svg>
  <p class="f-text" style="left:137px;top:217px">E-mail:<br>info@pelmarokvistaqueen.com</p>

  <div class="f-head" style="left:371px">Sign up for newsletter</div>
  <p class="f-text" style="left:377px;top:117px">Sign up to our mailing list</p>
  <div class="field" style="left:371px;top:148px;width:232px;height:34px;font-size:12px;color:#fff;background:#0a1c5a">Enter Email</div>
  <a class="btn" href="#" style="left:372px;top:193px;width:121px;height:35px;font-size:12px">Subscribe</a>

  <div class="f-head" style="left:680px;width:180px">Employment services</div>
  <p class="f-text" style="left:682px;top:140px;width:240px;line-height:22px">Sed ut perspiciatis unde omnis iste natus error sit voluptatem accusantium doloremque laudantium, totam rem aperiam, eaque ipsa</p>
  <div class="social" style="left:686px"></div>
  <div class="social" style="left:719px"></div>
  <div class="social" style="left:752px"></div>
  <div class="social" style="left:786px"></div>

  <div class="f-head" style="left:979px">Quick Link</div>
  <nav class="f-links">
    <a class="active" style="top:123px" href="#">Home</a>
    <a style="top:153px" href="#">About Us</a>
    <a style="top:183px" href="#">Our Services</a>
    <a style="top:213px" href="#">Our Blog</a>
    <a style="top:243px" href="#">Contact Us</a>
  </nav>

  <div class="abs" style="left:113px;top:320px;width:974px;height:1px;background:var(--line)"></div>
  <p class="copy">© 2022 &nbsp;<a href="#">Domain Monitoring</a> &nbsp;All Rights Reserved &nbsp;Disclaimer</p>
</footer>

</body>
</html>
```